Aerial Imaging and photgraphy business card

Design a business card with eye catching aerial photo of country side / landscape with a drone in the foreground.
Also contact details.

Target Market(s)

Aerial Imaging photography

Industry/Entity Type

Advertising

Contact Information for Business Card

Corwin
0412905316
Website http://www.skylarkvistas.com.au/
email address : skylarkvistas.com.au

Colors
e8f1ca
cadf82
9bcb3c
33a6d7
85cae6
cee9f5

Requirements
Must have
• High res photo
• KPV drone in the foreground Either T4200 and kpv Hovera or both
Nice to have
• high resolution landscape country photo on the front of the card with a KPV T4200 drone in the foreground.

```html
<!DOCTYPE html>
<html lang="en">
<head>
<meta charset="utf-8">
<title>Skylark Vistas – Business Card</title>
<link href="https://fonts.googleapis.com/css2?family=Roboto:wght@400;700&family=Roboto+Condensed:wght@400&display=swap" rel="stylesheet">
<style>
  :root {
    --backdrop: #e6e6e6;
    --card-white: #ffffff;
    --ink-dark: #3a3a3a;
    --ink-mid: #555555;
    --brand-green: #3aa23c;
    --accent-lime: #9bcb3c;
    --accent-blue: #33a6d7;
    --sky-light: #cee9f5;
    --sky-mid: #85cae6;
    --field-green: #6f9a4a;
    --field-dark: #3f5a2e;
  }
  * { box-sizing: border-box; margin: 0; padding: 0; }
  html, body { width: 1200px; height: 1200px; overflow: hidden; }
  body {
    background: var(--backdrop);
    font-family: "Roboto", Arial, sans-serif;
    position: relative;
  }
  .card {
    position: absolute;
    left: 162px;
    width: 876px;
    height: 500px;
    border-radius: 14px;
    overflow: hidden;
    background: var(--card-white);
    box-shadow: 0 6px 18px rgba(0,0,0,0.18);
  }
  .card--front { top: 60px; }
  .card--back { top: 640px; }

  .front-photo {
    width: 100%;
    height: 100%;
    background: linear-gradient(180deg,
      var(--sky-mid) 0%, var(--sky-light) 30%, #e9eef0 45%,
      #9fbf7a 58%, var(--field-green) 72%, var(--field-dark) 100%);
  }

  .back-art { position: absolute; inset: 0; }

  .brand {
    position: absolute;
    left: 56px;
    top: 64px;
    display: flex;
    align-items: center;
    gap: 14px;
  }
  .brand-dot {
    width: 46px; height: 46px;
    border-radius: 50%;
    background: var(--accent-blue);
  }
  .brand-name {
    font-weight: 700;
    font-size: 34px;
    color: var(--ink-dark);
    letter-spacing: 0.5px;
  }

  .person { position: absolute; left: 56px; top: 270px; }
  .person-name { font-weight: 700; font-size: 34px; color: var(--ink-dark); }
  .person-title { font-size: 16px; color: var(--ink-mid); margin-top: 2px; }

  .contacts {
    position: absolute;
    left: 56px;
    top: 365px;
    list-style: none;
    font-family: "Roboto Condensed", Arial, sans-serif;
    font-size: 20px;
    color: var(--ink-mid);
  }
  .contacts li { display: flex; align-items: center; gap: 14px; height: 32px; }
  .contacts svg { width: 18px; height: 18px; fill: var(--accent-blue); flex: none; }
  .web { font-weight: 400; color: var(--ink-dark); }
  .web strong { color: var(--brand-green); font-weight: 400; }
</style>
</head>
<body>

  <section class="card card--front">
    <div class="front-photo" role="img" aria-label="Aerial photo of green countryside and a lake under a blue sky, with a camera drone flying in the foreground"></div>
  </section>

  <section class="card card--back">
    <svg class="back-art" viewBox="0 0 876 500" width="876" height="500">
      <defs>
        <linearGradient id="sky-land" x1="0" y1="0" x2="0" y2="1">
          <stop offset="0" stop-color="#7fc3e6"/>
          <stop offset="0.45" stop-color="#cfe6f2"/>
          <stop offset="0.62" stop-color="#7f9fb0"/>
          <stop offset="0.8" stop-color="#6e8f5a"/>
          <stop offset="1" stop-color="#5d7c44"/>
        </linearGradient>
      </defs>
      <path d="M 372 0 Q 420 330 876 462 L 876 0 Z" fill="none" stroke="var(--accent-blue)" stroke-width="2" transform="translate(-24 0)"/>
      <path d="M 372 0 Q 420 330 876 462 L 876 0 Z" fill="var(--accent-lime)" transform="translate(-12 0)"/>
      <path d="M 372 0 Q 420 330 876 462 L 876 0 Z" fill="url(#sky-land)" role="img" aria-label="Photo of a camera drone in flight above rolling farmland and hills"/>
    </svg>

    <div class="brand">
      <span class="brand-dot"></span>
      <span class="brand-name">Skylark Vistas</span>
    </div>

    <div class="person">
      <h1 class="person-name">Corwin Reid</h1>
      <p class="person-title">Managing Director</p>
    </div>

    <ul class="contacts">
      <li>
        <svg viewBox="0 0 24 24"><path d="M6.6 10.8a15.1 15.1 0 0 0 6.6 6.6l2.2-2.2a1 1 0 0 1 1-.25 11.4 11.4 0 0 0 3.6.57 1 1 0 0 1 1 1V20a1 1 0 0 1-1 1A17 17 0 0 1 3 4a1 1 0 0 1 1-1h3.5a1 1 0 0 1 1 1c0 1.25.2 2.45.57 3.57a1 1 0 0 1-.25 1z"/></svg>
        <span>0412905316</span>
      </li>
      <li>
        <svg viewBox="0 0 24 24"><path d="M2 5h20v14H2z M2 5l10 8 10-8" stroke="#fff" stroke-width="1.5"/></svg>
        <span>hello@skylarkvistas.com.au</span>
      </li>
      <li>
        <svg viewBox="0 0 24 24"><circle cx="12" cy="12" r="10"/><path d="M2 12h20M12 2c3 3 3 17 0 20M12 2c-3 3-3 17 0 20" stroke="#fff" stroke-width="1.3" fill="none"/></svg>
        <span class="web">www.<strong>skylarkvistas</strong>.com.au</span>
      </li>
    </ul>
  </section>

</body>
</html>
```